Etiketten-Design für Imkerei
Fr. Haldorf überzeugte uns sehr schnell mit ihren Entwürfen. Der Dialog zwischen uns war sehr produktiv und es hat Spaß gemacht das Produkt reifen zu sehen.
Zielgruppe
Imkern.
Bienenvermehrung und Produkte aus dem Bienenvolk.
Zielgruppe: Jeder der Honig und Bienenprodukte mag.
Aufgabenstellung
Siehe Anhang.

```html
<!DOCTYPE html>
<html lang="de">
<head>
<meta charset="utf-8">
<title>Marlenti Bio-Imkerei – Etiketten</title>
<link rel="stylesheet" href="https://fonts.googleapis.com/css2?family=Roboto:wght@300;400;500&display=swap">
<style>
  :root{
    --page:#ffffff;
    --label-dark:#2a2a2a;
    --label-mid:#3a3a3a;
    --ink-light:#f2f2f2;
    --ink-soft:#cfcfcf;
    --brand-yellow:#f6c21c;
    --wald:#8cc63f;
    --propolis:#a39bd6;
    --blueten:#f7a721;
    --flag-red:#e0262b;
    --field-grey:#8a8a8a;
    --seal-green:#6ba539;
  }
  *{box-sizing:border-box;margin:0;padding:0}
  html,body{width:1200px;height:415px;overflow:hidden;background:var(--page)}
  body{position:relative;font-family:"Roboto",Arial,sans-serif;color:var(--ink-light)}

  .band,.strip{position:absolute;background:linear-gradient(180deg,var(--label-mid),var(--label-dark));overflow:hidden}
  .texture{position:absolute;inset:0;background:radial-gradient(ellipse at 50% 40%,rgba(255,255,255,.06),rgba(0,0,0,0) 70%)}

  .band--full{left:13px;top:207px;width:511px;height:150px}
  .band--front{top:207px;width:277px;height:150px}
  .band--propolis{left:587px}
  .band--blueten{left:902px}

  .info-panel{position:absolute;top:0;height:100%;font-size:6.2px;line-height:1.3;font-weight:300;color:var(--ink-light)}
  .info-panel--left{left:0;width:100px;padding:10px 6px 0 10px}
  .info-panel--right{right:0;width:91px;padding:16px 9px 0 6px;text-align:justify}
  .info-panel hr{border:0;border-top:.6px solid var(--ink-soft);margin:2px 0}
  .date-field{height:10px;background:var(--field-grey);margin-top:2px}
  .lot-field{height:6px;background:#9a9a9a;margin-top:3px;font-size:3.6px;color:#555;padding-left:2px;line-height:6px}
  .seals{display:flex;gap:5px;margin-top:4px;align-items:center}
  .seal-square{width:20px;height:15px;background:var(--seal-green)}
  .seal-round{width:15px;height:15px;border-radius:50%;background:#fff;border:2px solid #3a8f3e}
  .seal-code{font-size:5px;line-height:1.2;margin-top:3px}
  .fill-amount{position:absolute;left:6px;bottom:12px;font-size:7px;display:flex;align-items:baseline;gap:6px}
  .fill-amount strong{font-size:13px;font-weight:300}

  .front{position:absolute;top:0;height:100%;text-align:center}
  .band--full .front{left:100px;right:91px}
  .band--front .front{left:0;right:0}
  .brand{position:absolute;left:0;right:0;top:40px;display:flex;justify-content:center;align-items:center;gap:6px}
  .brand-dot{width:9px;height:9px;border-radius:50%;background:var(--brand-yellow)}
  .brand-name{font-size:36px;font-weight:400;color:var(--brand-yellow);letter-spacing:.5px;line-height:1}
  .brand-sub{position:absolute;left:0;right:0;top:86px;font-size:14px;font-weight:300;letter-spacing:3px;color:var(--ink-light)}
  .variety{position:absolute;left:50%;top:113px;width:38px;height:38px;margin-left:-19px;border-radius:50%;display:flex;justify-content:center;padding-top:15px;font-size:7px;color:#222}
  .variety::after{content:"";position:absolute;left:19px;top:25px;width:1px;height:10px;background:#fff;transform:rotate(-25deg)}
  .variety--wald{background:var(--wald)}
  .variety--propolis{background:var(--propolis)}
  .variety--blueten{background:var(--blueten)}

  .strip--tall{left:239px;top:13px;width:54px;height:176px}
  .strip--short{top:109px;width:51px;height:80px}
  .strip--propolis{left:694px}
  .strip--blueten{left:1012px}
  .strip-content{position:absolute;left:0;right:0;bottom:8px;display:flex;flex-direction:column;align-items:center}
  .flag{width:24px;height:16px;display:flex;flex-direction:column}
  .flag span{flex:1;background:var(--flag-red)}
  .flag span:nth-child(2){background:#fff}
  .strip-line{width:1px;height:12px;background:#fff;margin:4px 0 3px}
  .quality{font-size:6.2px;font-weight:300;line-height:1.25;text-align:center}
  .strip-mark{position:absolute;left:50%;top:16px;width:24px;height:24px;margin-left:-12px;border-radius:50%;background:var(--brand-yellow)}
</style>
</head>
<body>

  <section class="strip strip--tall">
    <div class="texture" role="img" aria-label="Dunkle Wabenstruktur"></div>
    <span class="strip-mark"></span>
    <div class="strip-content">
      <div class="strip-line"></div>
      <div class="flag"><span></span><span></span><span></span></div>
      <div class="strip-line"></div>
      <p class="quality">Österreichischer<br>Qualitätshonig</p>
    </div>
  </section>

  <section class="band band--full">
    <div class="texture" role="img" aria-label="Dunkle Wabenstruktur mit geschwungenen weißen Linien"></div>
    <div class="info-panel info-panel--left">
      <p>Trocken, Dunkel und vor<br>Wärme geschützt lagern</p>
      <hr>
      <p>Bio-Imkerei Marlenti<br>Wiesenweg 8<br>A-3100 Lindental<br>imkerei-marlenti.at</p>
      <hr>
      <p>Mindestens haltbar bis:</p>
      <div class="date-field"></div>
      <div class="lot-field">LOT-Nr.</div>
      <div class="seals"><span class="seal-square"></span><span class="seal-round"></span></div>
      <p class="seal-code">KS-BIO-017<br>Herkunft: Lindental</p>
    </div>
    <div class="front">
      <div class="brand"><span class="brand-dot"></span><span class="brand-name">Marlenti</span></div>
      <p class="brand-sub">BIO-IMKEREI</p>
      <div class="variety variety--wald">WALD</div>
    </div>
    <div class="info-panel info-panel--right">
      <p>Bienen bzw. Honig aus deiner Region unterstützt die Natur und Umwelt. Der Wert der Bestäubungsleistung übersteigt mehr als den 10-fachen Wert des Honigs. Eventuelle Kristallisation des Honigs ist ganz natürlich und beeinflusst nicht die Qualität.</p>
      <div class="fill-amount"><span>Füllmenge</span><strong>500g</strong></div>
    </div>
  </section>

  <section class="strip strip--short strip--propolis">
    <div class="strip-content">
      <div class="flag"><span></span><span></span><span></span></div>
      <div class="strip-line"></div>
      <p class="quality">Österreichischer<br>Qualitätshonig</p>
    </div>
  </section>
  <section class="band band--front band--propolis">
    <div class="texture" role="img" aria-label="Dunkle Wabenstruktur mit geschwungenen weißen Linien"></div>
    <div class="front">
      <div class="brand"><span class="brand-dot"></span><span class="brand-name">Marlenti</span></div>
      <p class="brand-sub">BIO-IMKEREI</p>
      <div class="variety variety--propolis">PROPOLIS</div>
    </div>
  </section>

  <section class="strip strip--short strip--blueten">
    <div class="strip-content">
      <div class="flag"><span></span><span></span><span></span></div>
      <div class="strip-line"></div>
      <p class="quality">Österreichischer<br>Qualitätshonig</p>
    </div>
  </section>
  <section class="band band--front band--blueten">
    <div class="texture" role="img" aria-label="Dunkle Wabenstruktur mit geschwungenen weißen Linien"></div>
    <div class="front">
      <div class="brand"><span class="brand-dot"></span><span class="brand-name">Marlenti</span></div>
      <p class="brand-sub">BIO-IMKEREI</p>
      <div class="variety variety--blueten">BLÜTEN</div>
    </div>
  </section>

</body>
</html>
```